Staff Falcons WIX Design Project - website for HR Professional Community

Redesign of website to incorporate new logo - we are looking for a web design partner - will include adhoc work going forward.

Current website - www.thestafffalcons.co.uk

The 'Onward to Radiant' content is not required on the new site.

Target Market(s)

HR professionals

Industry/Entity Type

Professional Network

Coding

Coded - Design and coding required

Requirements
Must have
• A partners page
Nice to have
• an events page

```html
<!DOCTYPE html>
<html lang="en">
<head>
<meta charset="utf-8">
<title>Staff Falcons – HR Professional Community</title>
<link href="https://fonts.googleapis.com/css2?family=Oswald:wght@300;400;500&family=Open+Sans:ital,wght@0,400;0,600;1,400&display=swap" rel="stylesheet">
<style>
:root{
  --orange:#ef861b;
  --orange-soft:#f7c99a;
  --dark:#1e1e1e;
  --black:#000;
  --white:#fff;
  --grey:#555;
  --light:#ececec;
  --line:#cfcfcf;
}
*{box-sizing:border-box;margin:0;padding:0}
html,body{width:1200px;height:5362px;overflow:hidden}
body{position:relative;background:var(--white);font-family:"Open Sans",Arial,sans-serif;color:var(--grey)}
.abs{position:absolute}
.heading{font-family:"Oswald","Arial Narrow",sans-serif;font-weight:400;letter-spacing:2px;color:#111;text-transform:uppercase}
.btn{position:absolute;display:flex;align-items:center;justify-content:center;font-family:"Oswald","Arial Narrow",sans-serif;font-size:13px;letter-spacing:.5px;text-transform:uppercase;white-space:nowrap}
.btn-outline{border:2px solid var(--orange);color:var(--orange)}
.btn-light{border:1px solid var(--white);color:var(--white)}
.photo{position:absolute}
/* header + hero */
.hero{position:absolute;left:0;top:0;width:1200px;height:632px;background:linear-gradient(180deg,#2a2824 0%,#3b3831 55%,#2b2822 100%)}
.hero-shade{position:absolute;inset:0;background:radial-gradient(ellipse at 50% 60%,rgba(120,110,95,.35),rgba(0,0,0,.2) 70%)}
.brand{position:absolute;display:flex;align-items:center;gap:10px;font-family:"Oswald","Arial Narrow",sans-serif;font-size:26px;letter-spacing:2px;color:var(--white);white-space:nowrap}
.brand .dot{width:22px;height:22px;border-radius:50%;background:var(--orange)}
.topbar{position:absolute;left:728px;top:28px;display:flex;align-items:center;gap:14px;font-size:13px;color:var(--white)}
.topbar .soc{width:13px;height:13px;border-radius:50%;background:var(--white)}
.nav{position:absolute;left:438px;top:88px;display:flex;gap:50px;font-family:"Oswald","Arial Narrow",sans-serif;font-size:14px;letter-spacing:.5px;color:var(--white)}
.nav .active{color:var(--orange)}
.header-rule{position:absolute;left:0;top:133px;width:1200px;height:1px;background:rgba(255,255,255,.25)}
.hero-title{position:absolute;left:0;top:258px;width:1200px;text-align:center;font-family:"Oswald","Arial Narrow",sans-serif;font-weight:300;font-size:40px;line-height:52px;letter-spacing:2px;color:var(--white)}
.hero-title em{font-style:normal;color:var(--orange)}
/* newsletter */
.newsletter{position:absolute;left:0;top:632px;width:1200px;height:138px;background:var(--orange);color:var(--white)}
.newsletter h2{position:absolute;left:146px;top:50px;font-family:"Oswald","Arial Narrow",sans-serif;font-weight:400;font-size:27px;letter-spacing:2px}
.newsletter .field{position:absolute;left:654px;top:56px;width:282px;height:30px;border-bottom:2px solid var(--white);font-size:13px}
/* services */
.service{position:absolute;top:873px;width:300px;text-align:center}
.service .photo{position:relative;margin:0 auto;width:226px;height:226px;border-radius:50%}
.service h3{margin-top:36px;font-size:28px}
.service p{margin:20px auto 0;width:250px;font-size:13.5px;line-height:19px;color:#444}
.service p b{color:var(--orange);font-weight:600}
.vline{position:absolute;top:873px;width:1px;height:420px;background:#e4e4e4}
/* about */
.dark-band{position:absolute;left:0;top:1826px;width:1200px;height:593px;background:linear-gradient(180deg,#262626,#191919)}
.about-frame{position:absolute;left:133px;top:1498px;width:330px;height:400px;background:var(--orange)}
.about-card{position:absolute;left:616px;top:1514px;width:432px;height:572px;background:var(--white)}
.about-card h2{position:absolute;left:48px;top:48px;font-size:46px}
.about-card .copy{position:absolute;left:50px;top:130px;width:340px;font-size:12.5px;line-height:19px;color:#333}
.about-card .copy p{margin-bottom:16px}
/* partners */
.partners-title{position:absolute;left:0;top:2188px;width:1200px;text-align:center;font-size:44px;color:var(--white)}
.partner{position:absolute;top:2296px;height:48px;background:rgba(255,255,255,.85);border-radius:4px}
/* team */
.team-title{position:absolute;left:0;top:2558px;width:1200px;text-align:center;font-size:46px}
.team-band{position:absolute;left:0;top:2760px;width:1200px;height:329px;background:var(--black)}
.member{position:absolute;top:2664px;width:260px;text-align:center;color:var(--white)}
.member .photo{position:relative;margin:0 auto;width:218px;height:218px;border-radius:50%}
.member h4{margin-top:28px;font-family:"Oswald","Arial Narrow",sans-serif;font-weight:400;font-size:25px;letter-spacing:1px}
.member span{display:block;margin-top:4px;font-size:15px;color:#bbb}
.member i{display:block;margin:16px auto 0;width:20px;height:20px;border-radius:50%;background:var(--orange)}
/* events */
.events-title{position:absolute;left:0;top:3176px;width:1200px;text-align:center;font-size:46px}
.event{position:absolute;border:2px solid #ddd;background:var(--white)}
.event h5{font-family:"Oswald","Arial Narrow",sans-serif;font-weight:400;font-size:28px;line-height:36px;color:#111}
.event p{font-size:13.5px;line-height:19px;color:#888}
.event-sm h5{font-size:24px;line-height:31px}
/* testimonial */
.quote-backdrop{position:absolute;left:786px;top:3910px;width:330px;height:370px;background:linear-gradient(135deg,var(--orange-soft),#fbe3cb)}
.quote-band{position:absolute;left:0;top:3879px;width:1067px;height:375px;background:var(--orange);color:var(--white)}
.quote-mark{position:absolute;left:120px;top:70px;font-family:"Oswald",sans-serif;font-size:260px;line-height:220px;font-weight:500}
.quote-text{position:absolute;left:302px;top:100px;width:700px;font-style:italic;font-size:21px;line-height:30px}
.quote-by{position:absolute;left:306px;top:260px;font-family:"Oswald",sans-serif;font-size:23px;letter-spacing:1.5px}
.quote-dots{position:absolute;left:940px;top:308px;display:flex;gap:9px}
.quote-dots i{width:9px;height:9px;border-radius:50%;background:var(--white)}
/* job board */
.jobs-title{position:absolute;left:466px;top:4440px;font-size:38px;letter-spacing:4px;font-weight:500;white-space:nowrap}
.jobs-list{position:absolute;left:468px;top:4510px;width:610px;list-style:none;font-size:16px;line-height:22px;color:#333}
.jobs-list li{position:relative;padding-left:22px;margin-bottom:22px}
.jobs-list li::before{content:"";position:absolute;left:0;top:6px;width:9px;height:9px;background:var(--orange);transform:rotate(45deg)}
/* footer */
.footer{position:absolute;left:0;top:4863px;width:1200px;height:499px;background:linear-gradient(180deg,#252320,#1a1917);color:var(--white)}
.footer .contact{position:absolute;left:350px;top:200px;display:flex;gap:52px;font-size:13px}
.footer .contact span{display:flex;align-items:center;gap:10px}
.form-field{position:absolute;width:246px;height:30px;border-bottom:1px solid rgba(255,255,255,.5);font-size:12px;font-weight:600}
.copyright{position:absolute;left:0;top:468px;width:1200px;text-align:center;font-size:12px}
</style>
</head>
<body>

<!-- Header & hero -->
<section class="hero">
  <div class="photo hero-shade" role="img" aria-label="Photo of HR professionals meeting around a table"></div>
  <div class="brand" style="left:80px;top:68px"><span class="dot"></span>STAFF FALCONS</div>
  <div class="topbar">
    <span class="soc"></span><span class="soc"></span>
    <svg width="14" height="11" viewBox="0 0 14 11"><rect x="0.5" y="0.5" width="13" height="10" fill="none" stroke="#fff"/><path d="M0.5 0.5 L7 6 L13.5 0.5" fill="none" stroke="#fff"/></svg>
    <span>hq@thestafffalcons.co.uk</span>
    <span class="btn btn-outline" style="position:relative;width:108px;height:32px;margin-left:10px">Newsletter</span>
  </div>
  <nav class="nav">
    <span class="active">HOME</span><span>JOB BOARD</span><span>OUR STORY</span><span>PARTNERS</span><span>EVENTS</span><span>CONTACT</span>
  </nav>
  <div class="header-rule"></div>
  <h1 class="hero-title">THE UK'S MOST VIBRANT <em>ONLINE</em><br><em>COMMUNITY</em> FOR HR PROFESSIONALS.</h1>
  <span class="btn btn-outline" style="left:480px;top:390px;width:114px;height:44px">View Jobs</span>
  <span class="btn btn-light" style="left:606px;top:390px;width:114px;height:44px">Sign Up Here</span>
</section>

<!-- Newsletter -->
<section class="newsletter">
  <h2>SIGN UP HERE FOR OUR NEWSLETTER</h2>
  <div class="field">Email:</div>
  <span class="btn btn-light" style="left:956px;top:50px;width:96px;height:40px;border-width:2px">Sign Up</span>
</section>

<!-- Services -->
<div class="vline" style="left:441px"></div>
<div class="vline" style="left:765px"></div>
<section class="service" style="left:127px">
  <div class="photo" role="img" aria-label="Photo of a cheerful group of colleagues" style="background:linear-gradient(135deg,#c9c4bd,#6d6a66)"></div>
  <h3 class="heading">Community</h3>
  <p>Our Gatherly Community Group enables you to connect with a fast-growing, highly engaged community of over 17k HR professionals</p>
</section>
<span class="btn btn-outline" style="left:163px;top:1328px;width:228px;height:46px;border-width:1.5px">Join our Gatherly group</span>
<section class="service" style="left:449px">
  <div class="photo" role="img" aria-label="Photo of a smiling professional woman" style="background:linear-gradient(135deg,#8a7a6e,#2f2a27)"></div>
  <h3 class="heading">Jobs</h3>
  <p>Get your HR job in front of 17k HR Professionals FREE job postings for members of our Gatherly group Open to non-members<br><b>ONLY £100+vat</b></p>
</section>
<span class="btn btn-outline" style="left:485px;top:1328px;width:228px;height:46px;border-width:1.5px">View our jobs board</span>
<section class="service" style="left:775px">
  <div class="photo" role="img" aria-label="Photo of a coaching session in an office" style="background:linear-gradient(135deg,#b3b1ad,#3d3b38)"></div>
  <h3 class="heading">Coaching</h3>
  <p>Our coaching club is currently over subscribed and we are not currently accepting requests for support. Doors are open now for registrations!</p>
</section>
<span class="btn btn-outline" style="left:811px;top:1328px;width:228px;height:46px;border-width:1.5px">Rregistrations</span>

<!-- About -->
<div class="dark-band"></div>
<div class="about-frame"></div>
<div class="photo" role="img" aria-label="Black and white portrait of the founder" style="left:152px;top:1514px;width:464px;height:572px;background:linear-gradient(160deg,#9a9a9a,#3a3a3a)"></div>
<article class="about-card">
  <h2 class="heading">Hey I'm Maya</h2>
  <div class="copy">
    <p>The search for your HR tribe is over!</p>
    <p>It's fair to say that this has been a tough year for our profession. More and more I am seeing HR helping others with their oxygen masks often at the expense of applying their own. HR is for life, not just for Covid! And I am left wondering "who is helping HR?" As human beings we are hard-wired for connection and we are at our best when we feel a sense of purpose and belonging.</p>
    <p>And this is where joining an on-line community like ours comes in. Because in a world where distancing has become the new norm, our community offers all HR Professionals a space to ask questions and seek support. I promise you that no question is ever a stupid question at Staff Falcons!</p>
  </div>
  <span class="btn btn-outline" style="left:50px;top:484px;width:142px;height:46px;border-width:1.5px">Read More</span>
</article>

<!-- Partners -->
<h2 class="heading partners-title">Partners</h2>
<div class="partner" style="left:188px;width:252px;height:30px;top:2304px"></div>
<div class="partner" style="left:468px;width:264px;height:42px"></div>
<div class="partner" style="left:752px;width:262px"></div>

<!-- Team -->
<h2 class="heading team-title">Meet the Team</h2>
<div class="team-band"></div>
<div class="member" style="left:174px">
  <div class="photo" role="img" aria-label="Black and white portrait of the founder" style="background:linear-gradient(160deg,#d0d0d0,#6b6b6b)"></div>
  <h4>MAYA THORNTON</h4><span>Founder Staff Falcons</span><i></i>
</div>
<div class="member" style="left:473px">
  <div class="photo" role="img" aria-label="Black and white portrait of the head of partnerships" style="background:linear-gradient(160deg,#e2e2e2,#7a7a7a)"></div>
  <h4>OWEN GARRICK</h4><span>Head of Partnerships</span><i></i>
</div>
<div class="member" style="left:775px">
  <div class="photo" role="img" aria-label="Black and white portrait of the creative editor" style="background:linear-gradient(160deg,#c4c4c4,#5a5a5a)"></div>
  <h4>NINA GARRICK</h4><span>Creative Editor</span><i></i>
</div>

<!-- Events -->
<h2 class="heading events-title">Latest Events</h2>
<article class="event" style="left:150px;top:3276px;width:436px;height:478px">
  <div class="photo" role="img" aria-label="Overhead photo of a team working at a desk" style="position:relative;width:432px;height:252px;background:linear-gradient(135deg,#8d8a85,#3e3b37)"></div>
  <h5 style="margin:22px 20px 0">Lorem ipsum dolor sit ametcons ectetur adipiscing eli</h5>
  <p style="margin:14px 26px 0">Lorem ipsum dolor sit amet, consectetur adipiscing elit, sed do eiusmod tempor incididunt ut labore et dolore magna aliqua.</p>
</article>
<article class="event event-sm" style="left:605px;top:3276px;width:446px;height:229px;display:flex">
  <div class="photo" role="img" aria-label="Photo of two colleagues reviewing charts" style="position:relative;width:216px;height:225px;background:linear-gradient(135deg,#d8d2c8,#8c8378)"></div>
  <div style="padding:32px 12px 0 28px;width:226px"><h5>Lorem ipsum dolo it ametconsctet</h5><p style="margin-top:14px">Lorem ipsum dolor sit amet, consectetur adi piscing elit, sed do eius mod tempor</p></div>
</article>
<article class="event event-sm" style="left:605px;top:3526px;width:446px;height:229px;display:flex">
  <div class="photo" role="img" aria-label="Photo of a businessman in a suit" style="position:relative;width:216px;height:225px;background:linear-gradient(135deg,#4d6a8a,#1c2c40)"></div>
  <div style="padding:32px 12px 0 28px;width:226px"><h5>Lorem ipsum dolo it ametconsctet</h5><p style="margin-top:14px">Lorem ipsum dolor sit amet, consectetur adi piscing elit, sed do eius mod tempor</p></div>
</article>

<!-- Testimonial -->
<div class="quote-backdrop" role="img" aria-label="Decorative dotted backdrop behind the testimonial"></div>
<section class="quote-band">
  <div class="quote-mark">“</div>
  <p class="quote-text">I love the Falcons group.&nbsp; It is a great place for like minded people to discuss their thoughts and ideas and to support each other.&nbsp; Also a great place for some light relief after a long week when reading the amusing stories and scenarios people in HR have to address"</p>
  <div class="quote-by">Rosalind. HR Professional</div>
  <div class="quote-dots"><i></i><i></i><i></i></div>
</section>

<!-- Job board -->
<div class="photo" role="img" aria-label="Illustration of the community mascot" style="left:135px;top:4378px;width:291px;height:385px;background:var(--orange);border-radius:46% 46% 20% 20%"></div>
<h2 class="heading jobs-title">The Staff Falcons Job Board!</h2>
<ul class="jobs-list">
  <li>Are you looking to share your HR roles with our audience?</li>
  <li>Are you an HR job seeker looking for your next adventure?</li>
  <li>We are fast becoming THE place to share and seek for HR jobs in the UK (and get this!... If you're a member of our Gatherly group you can share your jobs for FREE!)</li>
</ul>
<span class="btn btn-outline" style="left:474px;top:4708px;width:142px;height:46px;border-width:1.5px">View Jobs</span>

<!-- Footer -->
<footer class="footer">
  <div class="brand" style="left:520px;top:82px;font-size:28px"><span class="dot"></span>STAFF FALCONS</div>
  <div class="contact">
    <span><svg width="12" height="16" viewBox="0 0 12 16"><path d="M6 0C2.7 0 0 2.6 0 5.9 0 10 6 16 6 16s6-6 6-10.1C12 2.6 9.3 0 6 0z" fill="#fff"/><circle cx="6" cy="6" r="2.2" fill="#222"/></svg>14 Harrow Lane London E2 4QP</span>
    <span><svg width="14" height="11" viewBox="0 0 14 11"><rect x="0.5" y="0.5" width="13" height="10" fill="none" stroke="#fff"/><path d="M0.5 0.5 L7 6 L13.5 0.5" fill="none" stroke="#fff"/></svg>hq@thestafffalcons.co.uk</span>
  </div>
  <div class="form-field" style="left:350px;top:256px">Name:</div>
  <div class="form-field" style="left:606px;top:256px">Email:</div>
  <div class="form-field" style="left:350px;top:314px">Job Title:</div>
  <div class="form-field" style="left:606px;top:314px">Company:</div>
  <span class="btn" style="left:540px;top:384px;width:120px;height:38px;background:var(--orange);color:var(--white);font-size:12px">Submit Now</span>
  <div class="copyright">© 2022 All Rights are Reserved.</div>
</footer>

</body>
</html>
```